small business focused on life coaching and helping others "create better tomorrows" needs a website

The Pell R Group needs a website that focuses on life coaching and helping others "create better tomorrows"; This is a sole proprietorship so the focus should be on Marla, who has worn many hats and in an excellent position to help others. It should include 6 pages _ Home, Bio, Services, Book, Media, Contact Us and the logo that was created by Craft Plaza; also include testimonials from 5-6 individuals as well as why one might need these services (see file included)

Target Market(s)

Immigrants who need help navigating American system in the workplace, home or community, immigrant or at-risk students unable to communicate with their immigrant parents (due to language or unfamiliarity with the new culture) but would share with someone they trust, those in need of a mentor or help with career advancement or choices, those in need of help with public speaking or leadership development - Marla is someone who has worn many hats and in a position to help - extensive networking, an immigrant herself, former teacher, community leader, TV talk show host, author, mother, grandmother, etc.

Industry/Entity Type

Business

Coding

Coded - Design and coding required

Number of Pages Required

5+ page

Font styles to use
Sans Serif

Colors
cadf82
add136

Requirements
Must have
• visuals of Marla - present image of competency, caring, professionalism; need to include a 30-second video (in process of being produced) of Marla promoting the services, need to include 5-6 testimonials (which will be sent later). Please see the document that describes the different pages of the website and what should be included. Give the image of Marla's ability to help people GROW into a more productive self
Nice to have
• This is a sole proprietor business and as such, need to have people feel comfortable in who I am - trust is critical and that is why experience and competency should be shown

```html
<!DOCTYPE html>
<html lang="en">
<head>
<meta charset="utf-8">
<title>The Pell R Group – Creating Better Tomorrows</title>
<link href="https://fonts.googleapis.com/css2?family=Cinzel:wght@400;700&family=Open+Sans:ital,wght@0,400;0,600;0,700;1,400;1,700&display=swap" rel="stylesheet">
<style>
:root{
  --green:#8cc63e;
  --green-bright:#add136;
  --green-soft:#cadf82;
  --green-deep:#6fa52b;
  --black:#0b0b0b;
  --ink:#4a4a4a;
  --grey-card:#e6e6e6;
  --white:#ffffff;
}
*{margin:0;padding:0;box-sizing:border-box}
html,body{width:1200px;height:3838px;overflow:hidden;background:var(--white)}
body{font-family:"Open Sans",Arial,sans-serif;color:var(--ink)}
.page{position:relative;width:1200px;height:3838px;overflow:hidden}
.abs{position:absolute}

/* header */
.site-header{position:absolute;left:0;top:0;width:1200px;height:115px;background:var(--black)}
.brand{position:absolute;left:118px;top:18px;display:flex;flex-direction:column;align-items:center}
.brand-dot{width:46px;height:46px;border-radius:50%;border:3px solid var(--green)}
.brand-name{font-family:"Cinzel",serif;font-weight:700;color:var(--green);font-size:17px;margin-top:6px;white-space:nowrap}
.main-nav{position:absolute;left:392px;top:44px;display:flex;gap:34px;font-size:15px;font-weight:600;color:var(--white);text-transform:uppercase}
.main-nav .active{color:var(--green)}
.main-nav .active::before{content:"";display:inline-block;width:8px;height:8px;border-radius:50%;background:var(--green);margin-right:10px;vertical-align:2px}
.phone-btn{position:absolute;left:934px;top:32px;width:184px;height:50px;border-radius:25px;background:var(--green);color:var(--white);font-weight:700;font-size:17px;display:flex;align-items:center;justify-content:center;gap:10px}

/* hero */
.hero{position:absolute;left:0;top:115px;width:1200px;height:563px;background:linear-gradient(100deg,#3d3a2c 0%,#6b6a4a 35%,#b9a98a 60%,#7c6e5c 80%,#4b4a3a 100%)}
.hero-title{position:absolute;left:77px;top:122px;font-size:56px;font-weight:700;font-style:italic;color:var(--white)}
.hero-list{position:absolute;left:86px;top:205px;list-style:none;color:var(--white);font-size:16.5px;line-height:28.5px}
.hero-list li::before{content:"";display:inline-block;width:6px;height:6px;background:var(--white);border-radius:50%;margin-right:14px;vertical-align:3px}
.slide-arrow{position:absolute;width:50px;height:50px;border-radius:50%;background:rgba(0,0,0,.55);display:flex;align-items:center;justify-content:center}

/* focus band */
.focus-band{position:absolute;left:0;top:627px;width:1200px;height:256px;background:linear-gradient(180deg,rgba(173,209,54,.75) 0%,var(--green) 40%,var(--green) 100%)}
.focus-item{position:absolute;top:0;width:200px;text-align:center}
.focus-icon{width:112px;height:112px;margin:3px auto 0;border-radius:50%;background:var(--white);display:flex;align-items:center;justify-content:center;box-shadow:0 0 0 6px rgba(255,255,255,.35)}
.focus-label{font-family:"Cinzel",serif;color:var(--white);font-size:15px;line-height:30px;margin-top:26px;letter-spacing:.5px}

/* welcome */
.welcome-title{position:absolute;left:77px;top:950px;font-family:"Cinzel",serif;font-size:38px;font-weight:700;color:var(--green);white-space:nowrap}
.welcome-sub{position:absolute;left:77px;top:1003px;font-size:13px;font-weight:700;color:#222;letter-spacing:.6px}
.welcome-copy{position:absolute;left:77px;top:1038px;width:650px;font-size:13.5px;line-height:22px;color:#666}
.welcome-copy p+p{margin-top:18px}
.btn-solid{position:absolute;border-radius:24px;background:var(--green);color:var(--white);font-family:"Cinzel",serif;font-weight:700;font-size:17px;display:flex;align-items:center;justify-content:center}
.welcome-photo{position:absolute;left:767px;top:959px;width:356px;height:312px;background:linear-gradient(160deg,#5a4030 0%,#a7805e 45%,#ded3c6 70%,#7a5a40 100%)}

/* services */
.services{position:absolute;left:0;top:1335px;width:1200px;height:571px;background:linear-gradient(180deg,var(--green-bright) 0%,#9cc95a 50%,#7fb543 100%)}
.section-title{position:absolute;left:0;width:1200px;text-align:center;font-family:"Cinzel",serif;font-size:40px}
.section-sub{position:absolute;left:0;width:1200px;text-align:center;font-family:"Cinzel",serif;font-size:13px;font-weight:700;letter-spacing:1px}
.service-card{position:absolute;top:174px;width:195px;height:333px;border-radius:98px 98px 0 0;overflow:hidden;background:var(--black)}
.service-photo{width:100%;height:225px;background:linear-gradient(160deg,#2d2a28 0%,#8a6e58 50%,#d2c2b0 80%,#4a3f38 100%)}
.service-name{height:108px;display:flex;align-items:center;justify-content:center;text-align:center;font-family:"Cinzel",serif;font-weight:700;font-size:16px;line-height:22px;color:var(--white);padding:0 12px}

/* video */
.video{position:absolute;left:0;top:1906px;width:1200px;height:519px;background:linear-gradient(90deg,#1d1a18 0%,#3a3330 45%,#6d5a4c 70%,#3b302a 100%)}
.video-line{position:absolute;left:77px;top:205px;width:440px;font-size:27px;line-height:40px;color:var(--white)}
.play-btn{position:absolute;left:560px;top:226px;width:82px;height:82px;border-radius:50%;border:4px solid var(--white);background:var(--green);display:flex;align-items:center;justify-content:center}

/* testimonials */
.quote{position:absolute;font-size:14.5px;font-style:italic;line-height:21px;color:#666;padding:18px 22px 46px}
.quote.grey{background:var(--grey-card)}
.quote.green{background:var(--green);color:var(--white)}
.quote-name{position:absolute;right:22px;bottom:14px;font-style:normal;font-weight:700;font-size:17px;color:var(--green);letter-spacing:1px}
.quote.green .quote-name{color:var(--white)}
.quote-name::before{content:"";display:inline-block;width:18px;height:3px;background:currentColor;margin-right:8px;vertical-align:5px}

/* book */
.book{position:absolute;left:0;top:3044px;width:1200px;height:427px;background:linear-gradient(180deg,var(--green-bright) 0%,var(--green-bright) 50%,var(--green) 50%,var(--green-deep) 100%)}
.book-cover{position:absolute;left:166px;top:51px;width:205px;height:320px;background:linear-gradient(150deg,#f2ecec 0%,#e8c9cf 55%,#b96d7d 100%);box-shadow:8px 8px 14px rgba(0,0,0,.25)}
.book-title{position:absolute;left:430px;top:72px;font-family:"Cinzel",serif;font-size:38px;font-weight:700;color:var(--white)}
.book-author{position:absolute;left:430px;top:136px;font-size:16px;color:var(--white)}
.book-blurb{position:absolute;left:430px;top:174px;width:690px;font-size:14px;line-height:23px;color:var(--white)}
.btn-outline{position:absolute;left:430px;top:263px;width:184px;height:49px;border:2px solid var(--white);border-radius:25px;color:var(--white);font-family:"Cinzel",serif;font-weight:700;font-size:17px;display:flex;align-items:center;justify-content:center}

/* footer */
.site-footer{position:absolute;left:0;top:3471px;width:1200px;height:367px;background:var(--black);color:#cfcfcf}
.foot-brand{position:absolute;left:70px;top:42px;width:260px;text-align:center}
.foot-dot{width:96px;height:96px;margin:0 auto;border-radius:50%;border:4px solid var(--green)}
.foot-name{font-family:"Cinzel",serif;font-weight:700;color:var(--green);font-size:22px;margin-top:12px}
.social{position:absolute;top:200px;width:38px;height:38px;border-radius:50%;border:2px solid var(--green)}
.foot-head{position:absolute;top:36px;font-family:"Cinzel",serif;color:var(--green);font-size:16px;letter-spacing:1px}
.foot-links{position:absolute;left:363px;top:74px;list-style:none;font-size:14px;line-height:32px;color:var(--white)}
.foot-links li::before{content:"";display:inline-block;width:5px;height:5px;border-radius:50%;background:var(--green);margin-right:16px;vertical-align:3px}
.foot-text{position:absolute;left:581px;top:74px;width:250px;font-size:14px;line-height:22px;color:var(--white)}
.foot-input{position:absolute;left:581px;top:167px;width:245px;height:38px;background:var(--white);font-size:13px;color:#888;padding:10px}
.contact-row{position:absolute;left:870px;display:flex;gap:14px;font-size:14px;line-height:22px;color:var(--white)}
.contact-row strong{color:var(--green);font-weight:600}
.copyright{position:absolute;left:0;top:310px;width:1200px;height:57px;border-top:1px solid #222;text-align:center;font-size:14px;line-height:57px;color:var(--white)}
</style>
</head>
<body>
<div class="page">

  <header class="site-header">
    <div class="brand"><span class="brand-dot"></span><span class="brand-name">The Pell R Group</span></div>
    <nav class="main-nav">
      <span class="active">Home</span><span>Bio</span><span>Services</span><span>Book</span><span>Media</span><span>Contact Us</span>
    </nav>
    <div class="phone-btn">
      <svg width="18" height="18" viewBox="0 0 24 24"><path fill="#fff" d="M6.6 10.8a15 15 0 0 0 6.6 6.6l2.2-2.2c.3-.3.7-.4 1-.2 1.1.4 2.3.6 3.6.6.6 0 1 .4 1 1V20c0 .6-.4 1-1 1A17 17 0 0 1 3 4c0-.6.4-1 1-1h3.5c.6 0 1 .4 1 1 0 1.3.2 2.5.6 3.6.1.3 0 .7-.2 1z"/></svg>
      (555) 014-2290
    </div>
  </header>

  <section class="hero" role="img" aria-label="Marla holding her book in a sunlit flower field">
    <h1 class="hero-title">The Pell R Group</h1>
    <ul class="hero-list">
      <li>Are you an immigrant needing help navigating the American system?</li>
      <li>Are you an immigrant parent unable to support your children's career choice or life issue ?</li>
      <li>Do you need help with your job search?</li>
      <li>Are you considering a career change?</li>
      <li>Are You Struggling To Balance Demands Of Work, Home And Life?</li>
      <li>Do you need help with time management, leadership development, etc.?</li>
      <li>Are you worried about your teenager's change in behavior?</li>
      <li>Is your family struggling with an addiction, mental health issue?</li>
    </ul>
    <div class="slide-arrow" style="left:13px;top:249px"><svg width="20" height="20" viewBox="0 0 20 20"><path d="M10 4 4 10l6 6M16 4l-6 6 6 6" fill="none" stroke="#fff" stroke-width="2"/></svg></div>
    <div class="slide-arrow" style="left:1137px;top:249px"><svg width="20" height="20" viewBox="0 0 20 20"><path d="M10 4l6 6-6 6M4 4l6 6-6 6" fill="none" stroke="#fff" stroke-width="2"/></svg></div>
  </section>

  <section class="focus-band">
    <div class="focus-item" style="left:79px">
      <div class="focus-icon"><svg width="58" height="58" viewBox="0 0 58 58" fill="none" stroke="#333" stroke-width="2.5"><circle cx="24" cy="24" r="16"/><circle cx="24" cy="20" r="5"/><path d="M15 33c2-6 16-6 18 0M36 36l14 14"/></svg></div>
      <div class="focus-label">Careers</div>
    </div>
    <div class="focus-item" style="left:291px">
      <div class="focus-icon"><svg width="58" height="58" viewBox="0 0 58 58" fill="none" stroke="#333" stroke-width="2.5"><circle cx="29" cy="29" r="20"/><path d="M9 29h40M29 9c-8 10-8 30 0 40M29 9c8 10 8 30 0 40"/></svg></div>
      <div class="focus-label">Acculturation</div>
    </div>
    <div class="focus-item" style="left:496px">
      <div class="focus-icon"><svg width="58" height="58" viewBox="0 0 58 58" fill="none" stroke="#333" stroke-width="2.5"><circle cx="16" cy="20" r="5"/><circle cx="29" cy="16" r="5"/><circle cx="42" cy="20" r="5"/><path d="M8 44V32c0-4 4-6 8-6s8 2 8 6M21 44V28c0-4 4-6 8-6s8 2 8 6v16M34 32c0-4 4-6 8-6s8 2 8 6v12"/></svg></div>
      <div class="focus-label">Leadership<br>Development</div>
    </div>
    <div class="focus-item" style="left:706px">
      <div class="focus-icon"><svg width="58" height="58" viewBox="0 0 58 58" fill="none" stroke="#333" stroke-width="2.5"><circle cx="29" cy="13" r="5"/><path d="M21 28c0-5 4-8 8-8s8 3 8 8M12 30h34M16 30l4 18h18l4-18"/></svg></div>
      <div class="focus-label">Public<br>Speaking</div>
    </div>
    <div class="focus-item" style="left:916px">
      <div class="focus-icon"><svg width="58" height="58" viewBox="0 0 58 58" fill="none" stroke="#333" stroke-width="2.5"><path d="M29 50V26M29 34l-9-7M29 30l9-6"/><path d="M14 28c-6-8 2-18 10-16 3-6 13-6 16 0 8-2 14 8 8 16z"/></svg></div>
      <div class="focus-label">Inter-Generationa<br>l Relations</div>
    </div>
  </section>

  <section>
    <h2 class="welcome-title">Welcome To The Pell R Group</h2>
    <div class="welcome-sub">CREATING BETTER TOMORROWS</div>
    <div class="welcome-copy">
      <p>Life coach (this is a business that is focused on the individual – Marla Pell). As such, need to present Marla as a mature professional with extensive experience in working with people and someone who has been very effective in getting things done.</p>
      <p>Aside from her personal experience as an immigrant, parent and grandparent, Marla has decades of experience as a teacher and administrator in a number of school systems, Director of a countywide agency, community leader heading a national organization with chapters nationally.</p>
    </div>
    <div class="btn-solid" style="left:77px;top:1223px;width:186px;height:48px">Learn More</div>
    <div class="welcome-photo" role="img" aria-label="Marla and a guest on a television cooking set"></div>
  </section>

  <section class="services" role="img" aria-label="Soft green backdrop of a coffee cup on a desk">
    <h2 class="section-title" style="top:50px;color:var(--white)">Services We Provide You</h2>
    <div class="section-sub" style="top:104px;color:var(--white)">WHAT WE DO</div>
    <div class="service-card" style="left:82px"><div class="service-photo" role="img" aria-label="Marla coaching a client at a desk"></div><div class="service-name">Life Coaching – Write Up</div></div>
    <div class="service-card" style="left:289px"><div class="service-photo" role="img" aria-label="Marla seated at a community event"></div><div class="service-name">Acculturation</div></div>
    <div class="service-card" style="left:496px"><div class="service-photo" role="img" aria-label="Marla with family members at a table"></div><div class="service-name">Intergeneratio nal Relations</div></div>
    <div class="service-card" style="left:714px"><div class="service-photo" role="img" aria-label="Group of leaders posing at a gala"></div><div class="service-name">Leadership Development &amp; Public Speaking</div></div>
    <div class="service-card" style="left:923px"><div class="service-photo" role="img" aria-label="Marla with a colleague at an organization meeting"></div><div class="service-name">Organizationa l Management</div></div>
  </section>

  <section class="video" role="img" aria-label="Video still of Marla speaking at a podium microphone">
    <p class="video-line">Are you an immigrant parent unable to support your children's career choice or life issue</p>
    <div class="play-btn"><svg width="30" height="30" viewBox="0 0 30 30"><path d="M9 5l17 10-17 10z" fill="#fff"/></svg></div>
  </section>

  <section>
    <h2 class="section-title" style="top:2478px;color:var(--green);font-weight:700">What Our Client Say About Us</h2>
    <div class="section-sub" style="top:2532px;color:#222">TESTIMONIALS</div>

    <div class="quote grey" style="left:77px;top:2589px;width:378px;height:366px">
      Marla Is My "Go-To" Person For Just About Anything. She Has Been A Significant Support In My Acculturation Into Western Culture – Helping Me Navigate The Many Aspects Of Life's Journey. Through Her Guidance, I Have Gained Much Confidence In Myself And In My Approach To Resolving Issues. Her Immigrant Experience Helps Her Understand My Challenges. Her Decades Of Living And Working In This Country Enables Her To Provide Advice Based On Personal Experience.
      <span class="quote-name">RITA P</span>
    </div>
    <svg class="abs" style="left:415px;top:2954px" width="42" height="30" viewBox="0 0 42 30"><path d="M0 0h40v30z" fill="var(--grey-card)"/></svg>

    <div class="quote green" style="left:466px;top:2589px;width:322px;height:190px">
      Thank You To Ms. Marla For Helping Me With Getting A Good Job With Benefits – And Then Being Promoted From That Job Two Years Later. I Met Ms. Marla While Painting Her House. ...
      <span class="quote-name">JOSE D</span>
    </div>
    <svg class="abs" style="left:466px;top:2778px" width="34" height="24" viewBox="0 0 34 24"><path d="M0 0h34L0 24z" fill="var(--green)"/></svg>

    <div class="quote grey" style="left:801px;top:2589px;width:317px;height:190px">
      Marla Was Instrumental In Motivating Me To Pursue My Dream Of Being A Teacher After Years Of Procrastinating. Being An Asian American, She Understood My Commitment To Family And Guided....
      <span class="quote-name">SAM L</span>
    </div>
    <svg class="abs" style="left:801px;top:2778px" width="34" height="24" viewBox="0 0 34 24"><path d="M0 0h34L0 24z" fill="var(--grey-card)"/></svg>

    <div class="quote grey" style="left:466px;top:2810px;width:652px;height:142px">
      Our Family Was In A Crisis Situation Dealing With The Addiction Of Our Son. Marla Was A Tremendous Source Of Support And Comfort During Our Time Of Desperate Need. She Understood And Guided Us And Our Son Through The Roller...
      <span class="quote-name">JENNIFER P</span>
    </div>
  </section>

  <section class="book">
    <div class="book-cover" role="img" aria-label="Cover of Marla's memoir book"></div>
    <h2 class="book-title">The Pell R Group Book</h2>
    <div class="book-author">Author : Marla</div>
    <p class="book-blurb">"From Wash Basin to Boardroom: My Family Laundry Story in America" is the story of an immigrant family's struggles to survive the challenges of life in a strange country as seen through the eyes of the oldest daughter. The joys, frustrations, and challenges of a young girl.</p>
    <div class="btn-outline">Learn More</div>
    <svg class="abs" style="left:24px;top:192px" width="22" height="36" viewBox="0 0 22 36"><path d="M18 3 4 18l14 15" fill="none" stroke="#fff" stroke-width="4"/></svg>
    <svg class="abs" style="left:1154px;top:192px" width="22" height="36" viewBox="0 0 22 36"><path d="M4 3l14 15L4 33" fill="none" stroke="#fff" stroke-width="4"/></svg>
  </section>

  <footer class="site-footer">
    <div class="foot-brand"><div class="foot-dot"></div><div class="foot-name">The Pell R Group</div></div>
    <span class="social" style="left:122px"></span>
    <span class="social" style="left:178px"></span>
    <span class="social" style="left:229px"></span>

    <div class="foot-head" style="left:363px">Sitemap</div>
    <ul class="foot-links"><li>Home</li><li>Bio</li><li>Services</li><li>Book</li><li>Midea</li><li>Contact</li></ul>

    <div class="foot-head" style="left:581px">Newsletter</div>
    <p class="foot-text">Would you like to receive exclusive access to articles, white papers and our regular monthly newsletter?</p>
    <div class="foot-input">Enter Email *</div>
    <div class="btn-solid" style="left:581px;top:218px;width:245px;height:42px">Subscribe</div>

    <div class="foot-head" style="left:870px">Contact Us</div>
    <div class="contact-row" style="top:74px">
      <svg width="18" height="24" viewBox="0 0 18 24"><path d="M9 0a9 9 0 0 0-9 9c0 7 9 15 9 15s9-8 9-15a9 9 0 0 0-9-9zm0 12a3 3 0 1 1 0-6 3 3 0 0 1 0 6z" fill="var(--green)"/></svg>
      <div><strong>The Pell R Group</strong><br>410 Quiet Harbor Lane,<br>Fairview, ST 00000</div>
    </div>
    <div class="contact-row" style="top:178px">
      <svg width="18" height="18" viewBox="0 0 24 24"><path fill="var(--green)" d="M6.6 10.8a15 15 0 0 0 6.6 6.6l2.2-2.2c.3-.3.7-.4 1-.2 1.1.4 2.3.6 3.6.6.6 0 1 .4 1 1V20c0 .6-.4 1-1 1A17 17 0 0 1 3 4c0-.6.4-1 1-1h3.5c.6 0 1 .4 1 1 0 1.3.2 2.5.6 3.6.1.3 0 .7-.2 1z"/></svg>
      <div>(555) 014-2290</div>
    </div>
    <div class="contact-row" style="top:225px">
      <svg width="18" height="14" viewBox="0 0 18 14"><rect width="18" height="14" fill="var(--green)"/><path d="M0 0l9 7 9-7" fill="none" stroke="#000" stroke-width="1.5"/></svg>
      <div>marla.pell@example.net</div>
    </div>

    <div class="copyright">©The Pell R Group - 2017 All Right Reserved.</div>
  </footer>

</div>
</body>
</html>
```